Business Card Creation

I am looking for a business card with a double take look... I upload a logo I would like used for its creation. We are an environmental firm that handles indoor air quality, water damages, fire damages, mold, HVAC contaminants, inspections and testing.

I just want to say that all the submissions are exactly what we were looking for and that everything from the font, layout and colors are amazing... Keep up the good work.

Business

```html
<!DOCTYPE html>
<html lang="en">
<head>
<meta charset="utf-8">
<title>R &amp; M Consulting — Business Cards</title>
<link rel="stylesheet" href="https://fonts.googleapis.com/css2?family=Arimo:wght@400&family=Caveat:wght@400&display=swap">
<style>
  :root {
    --bg: #ece9e4;
    --card: #f4f4f4;
    --card-edge: #e2e2e2;
    --ink: #4a4a4a;
    --ink-soft: #6b6b6b;
    --line: #5a5a5a;
    --green: #2aa563;
    --map-light: #f0f0f0;
    --map-dark: #dcdcdc;
  }
  * { margin: 0; padding: 0; box-sizing: border-box; }
  html, body { width: 900px; height: 1200px; overflow: hidden; }
  body { background: var(--bg); position: relative; font-family: "Arimo", Arial, sans-serif; }

  .card {
    position: absolute;
    width: 450px;
    height: 266px;
    background: radial-gradient(ellipse at 50% 40%, #fbfbfb 0%, var(--card) 60%, var(--card-edge) 100%);
    box-shadow: 0 2px 6px rgba(0,0,0,0.12);
  }
  .card--front-a { left: 75px;  top: 23px; }
  .card--back-a  { left: 375px; top: 319px; }
  .card--front-b { left: 75px;  top: 615px; }
  .card--back-b  { left: 375px; top: 911px; }

  /* Front */
  .brand {
    position: absolute;
    inset: 0;
    display: flex;
    flex-direction: column;
    align-items: center;
    justify-content: center;
    gap: 22px;
  }
  .brand__dot {
    width: 96px;
    height: 96px;
    border-radius: 50%;
    background: var(--green);
  }
  .brand__name {
    font-size: 28px;
    color: var(--ink);
    letter-spacing: 0.5px;
  }

  /* Back */
  .arrow { position: absolute; left: 0; top: 0; }
  .headline {
    position: absolute;
    left: 270px;
    top: 22px;
    font-family: "Caveat", cursive;
    color: var(--ink-soft);
    line-height: 1;
  }
  .headline__main { font-size: 30px; transform: rotate(6deg); display: block; }
  .headline__sub { font-size: 20px; display: block; margin-top: 2px; }
  .headline__role { font-size: 13px; display: block; margin: 2px 0 0 6px; transform: rotate(4deg); }

  .map {
    position: absolute;
    left: 200px;
    top: 100px;
    width: 200px;
    height: 130px;
    background: linear-gradient(160deg, var(--map-light), var(--map-dark));
    border-radius: 6px;
  }
  .map__pin { position: absolute; left: 70px; top: 18px; }

  .contact {
    position: absolute;
    left: 32px;
    bottom: 32px;
    font-size: 12px;
    color: var(--ink-soft);
    line-height: 20px;
  }
  .contact__company { font-size: 13px; color: var(--ink); }
  .contact__phone { font-size: 10px; margin-top: 2px; }
</style>
</head>
<body>

  <section class="card card--front-a">
    <div class="brand">
      <span class="brand__dot"></span>
      <span class="brand__name">R &amp; M Consulting, Inc.</span>
    </div>
  </section>

  <section class="card card--back-a">
    <svg class="arrow" width="450" height="266" viewBox="0 0 450 266" aria-hidden="true">
      <path d="M92 150 Q140 70 250 52" fill="none" stroke="var(--line)" stroke-width="1.8"/>
      <path d="M238 42 L254 52 L238 60" fill="none" stroke="var(--line)" stroke-width="1.8"/>
    </svg>
    <div class="headline">
      <span class="headline__main">You can find us</span>
      <span class="headline__sub">in here</span>
    </div>
    <div class="map" role="img" aria-label="Hand-drawn street sketch showing the office location on the avenue">
      <svg class="map__pin" width="26" height="38" viewBox="0 0 26 38" aria-hidden="true">
        <path d="M13 1 C6 1 1 6 1 13 C1 22 13 37 13 37 C13 37 25 22 25 13 C25 6 20 1 13 1 Z" fill="var(--ink-soft)"/>
        <circle cx="13" cy="13" r="5" fill="var(--card)"/>
      </svg>
    </div>
    <div class="contact">
      <div class="contact__company">R &amp; M Consulting, Inc.</div>
      <div>www.website.com</div>
      <div>email@website.com</div>
      <div class="contact__phone">000 000 000</div>
    </div>
  </section>

  <section class="card card--front-b">
    <div class="brand">
      <span class="brand__dot"></span>
      <span class="brand__name">R &amp; M Consulting, Inc.</span>
    </div>
  </section>

  <section class="card card--back-b">
    <svg class="arrow" width="450" height="266" viewBox="0 0 450 266" aria-hidden="true">
      <path d="M92 150 Q140 70 250 52" fill="none" stroke="var(--line)" stroke-width="1.8"/>
      <path d="M238 42 L254 52 L238 60" fill="none" stroke="var(--line)" stroke-width="1.8"/>
    </svg>
    <div class="headline">
      <span class="headline__main">Nora Whitfield</span>
      <span class="headline__role">Human Resources</span>
    </div>
    <div class="map" role="img" aria-label="Hand-drawn street sketch showing the office location on the avenue">
      <svg class="map__pin" width="26" height="38" viewBox="0 0 26 38" aria-hidden="true">
        <path d="M13 1 C6 1 1 6 1 13 C1 22 13 37 13 37 C13 37 25 22 25 13 C25 6 20 1 13 1 Z" fill="var(--ink-soft)"/>
        <circle cx="13" cy="13" r="5" fill="var(--card)"/>
      </svg>
    </div>
    <div class="contact">
      <div class="contact__company">R &amp; M Consulting, Inc.</div>
      <div>www.website.com</div>
      <div>email@website.com</div>
      <div class="contact__phone">000 000 000</div>
    </div>
  </section>

</body>
</html>
```